Engineering Consultant Business Card

I'm starting a new business as a high-end engineering consultant in a niche field. I've attached the jpg for my logo plus the branding guideline document that I've been following. You can see my business website here: www.tarvikworks.com
I'd like a business card that has the logo on one side, then the other side has (in any order): Tarvik Works, Inc.
Dana Whitlock
President and Chief EMC Engineer
www.tarvikworks.com
dana@tarvikworks.com
Optional: motto "We will solve your EMC problems as early as possible—ideally before they even start."
I'm not planning on including a phone number
Target Market(s)
Businesses, especially makers of electronics hardware
Industry/Entity Type
Electrical engineering
Contact Information for Business Card
Company name, my name, website, email

```html
<!DOCTYPE html>
<html lang="en">
<head>
<meta charset="utf-8">
<title>Tarvik Works, Inc. — Business Card</title>
<link rel="stylesheet" href="https://fonts.googleapis.com/css2?family=Public+Sans:wght@400;600&family=Source+Serif+4:ital@1&display=swap">
<style>
  :root {
    --backdrop: #c6c6c6;
    --brand-blue: #2f4699;
    --brand-blue-light: #3a52a6;
    --card-pale: #eaf3f4;
    --accent-cyan: #4aa8c8;
    --ink: #111111;
    --link-blue: #2a3f9a;
    --motto-grey: #777777;
    --white: #ffffff;
  }
  * { margin: 0; padding: 0; box-sizing: border-box; }
  html, body {
    width: 1200px; height: 1200px; overflow: hidden;
    background: var(--backdrop);
    font-family: "Public Sans", Arial, sans-serif;
  }
  .card {
    position: absolute; left: 226px; width: 746px; height: 435px;
    border-radius: 25px; overflow: hidden;
  }
  .card-front { top: 106px; background: var(--brand-blue); }
  .card-back { top: 611px; background: var(--card-pale); }

  .front-ring {
    position: absolute; left: 360px; top: -40px; width: 440px; height: 440px;
    border-radius: 50%; border: 3px solid var(--brand-blue-light);
  }
  .front-wordmark {
    position: absolute; left: 60px; top: 140px;
    font-size: 110px; font-weight: 600; line-height: 1;
    color: var(--brand-blue-light); white-space: nowrap;
  }
  .front-url {
    position: absolute; left: 0; right: 0; top: 380px;
    text-align: center; font-size: 21px; color: var(--white);
  }

  .back-wordmark {
    position: absolute; left: 60px; top: 198px; width: 290px;
    display: flex; align-items: center; gap: 12px;
    font-size: 34px; font-weight: 600; color: var(--brand-blue); white-space: nowrap;
  }
  .back-wordmark .mark-dot {
    width: 34px; height: 34px; border-radius: 50%; background: var(--brand-blue); flex: none;
  }
  .divider {
    position: absolute; left: 372px; top: 149px; width: 2px; height: 137px;
    background: var(--accent-cyan);
  }
  .contact { position: absolute; left: 414px; top: 166px; }
  .contact-name { font-size: 28px; font-weight: 600; color: var(--accent-cyan); line-height: 34px; }
  .contact-title { font-size: 20px; color: var(--ink); margin-top: 2px; }
  .contact-email {
    display: flex; align-items: center; gap: 12px; margin-top: 16px;
    font-size: 19px; color: var(--link-blue);
  }
  .contact-email span { border-bottom: 1.5px solid var(--link-blue); padding-bottom: 3px; }
  .motto {
    position: absolute; left: 0; right: 0; top: 354px;
    text-align: center; font-family: "Source Serif 4", Georgia, serif;
    font-style: italic; font-size: 21px; line-height: 29px; color: var(--motto-grey);
  }
</style>
</head>
<body>
  <section class="card card-front" aria-label="Card front">
    <div class="front-ring"></div>
    <div class="front-wordmark">Tarvik Works</div>
    <p class="front-url">tarvikworks.com</p>
  </section>

  <section class="card card-back" aria-label="Card back">
    <div class="back-wordmark"><span class="mark-dot"></span>Tarvik Works</div>
    <div class="divider"></div>
    <div class="contact">
      <p class="contact-name">Dana Whitlock</p>
      <p class="contact-title">President and Chief</p>
      <p class="contact-email">
        <svg width="22" height="16" viewBox="0 0 22 16" aria-hidden="true">
          <rect x="1.5" y="1.5" width="19" height="13" fill="none" stroke="#111" stroke-width="2.4"/>
          <path d="M1.5 1.5 L11 9 L20.5 1.5" fill="none" stroke="#111" stroke-width="2.4"/>
        </svg>
        <span>dana@tarvikworks.com</span>
      </p>
    </div>
    <p class="motto">We will solve your EMC problems as early as possible<br>— ideally before they even start.</p>
  </section>
</body>
</html>
```